RT Website Home Page Design

The task is to develop a winning design for a replacement website for our client RT Plumbing, Heating, AC & Remodeling. ct

```html
<!DOCTYPE html>
<html lang="en">
<head>
<meta charset="utf-8">
<title>RT Plumbing — Home</title>
<link rel="stylesheet" href="https://fonts.googleapis.com/css2?family=Montserrat:wght@400;600;700;800&family=Open+Sans:wght@400;600;700&display=swap">
<style>
:root{
  --navy:#0f1f4b;
  --yellow:#f7cf1c;
  --yellow-soft:#fbefb8;
  --cream:#fdf8e4;
  --grey-bg:#f1f1f1;
  --tile-icon:#9b9b9b;
  --text:#2c2c2c;
  --muted:#666;
  --white:#fff;
  --line:#2c3d6e;
}
*{box-sizing:border-box;margin:0;padding:0}
html,body{width:1200px;height:2792px;overflow:hidden}
body{font-family:"Open Sans",Arial,sans-serif;color:var(--text);background:var(--white);position:relative}
h1,h2,h3{font-family:"Montserrat",Arial,sans-serif}
.ph{position:absolute;border-radius:2px}

/* header */
.topbar{position:absolute;left:0;top:0;width:1200px;height:68px;background:var(--white)}
.brand{position:absolute;display:flex;align-items:center;gap:10px}
.brand-dot{width:30px;height:30px;border-radius:50%;background:var(--yellow);flex:none}
.brand-name{font-family:"Montserrat",Arial,sans-serif;font-weight:700;color:var(--navy);font-size:20px;white-space:nowrap}
.topbar .brand{left:40px;top:19px}
.serving{position:absolute;left:430px;top:8px;width:340px;text-align:center;font-size:11px;font-weight:600;color:var(--navy)}
.top-btns{position:absolute;left:470px;top:30px;display:flex;gap:10px}
.btn-y{background:var(--yellow);color:var(--navy);font-family:"Montserrat",Arial,sans-serif;font-weight:700;font-size:10px;padding:6px 14px;border-radius:2px}
.btn-n{background:var(--navy);color:var(--white);font-family:"Montserrat",Arial,sans-serif;font-weight:700;font-size:10px;padding:6px 14px;border-radius:2px}
.phones{position:absolute;right:40px;top:12px;font-size:12px;font-weight:700;color:var(--navy);line-height:1.6}
.phones div{display:flex;align-items:center;gap:6px}
.nav{position:absolute;left:0;top:68px;width:1200px;height:28px;background:var(--navy);display:flex;align-items:center;padding-left:48px}
.nav a{font-family:"Montserrat",Arial,sans-serif;font-size:10.5px;font-weight:600;color:var(--white);text-decoration:none;padding:0 17px;height:28px;line-height:28px}
.nav a.active{background:var(--yellow);color:var(--navy)}

/* hero */
.hero{position:absolute;left:0;top:96px;width:1200px;height:504px;background:var(--navy)}
.hero-copy{position:absolute;left:60px;top:170px}
.hero-copy .kicker{color:var(--white);font-size:19px;font-family:"Montserrat",Arial,sans-serif}
.hero-copy h1{color:var(--yellow);font-size:42px;font-weight:800;line-height:1.12;margin-top:6px}
.hero-copy .btn-y{display:inline-block;margin-top:20px;font-size:9.5px;border-radius:14px;padding:7px 16px}

/* services */
.services{position:absolute;left:0;top:600px;width:1200px;height:560px}
.services h2{position:absolute;left:56px;top:70px;font-size:26px;font-weight:800;color:var(--navy)}
.svc-grid{position:absolute;left:56px;top:130px;width:630px;display:grid;grid-template-columns:1fr 1fr;row-gap:20px;column-gap:16px}
.svc{display:flex;align-items:center;height:52px;background:var(--grey-bg)}
.svc-ico{width:52px;height:52px;background:var(--tile-icon);display:flex;align-items:center;justify-content:center}
.svc-label{flex:1;padding-left:14px;font-size:13px;font-weight:600;color:var(--navy);font-family:"Montserrat",Arial,sans-serif;line-height:1.2}
.svc-arrow{width:48px;height:52px;background:var(--yellow);display:flex;align-items:center;justify-content:center}
.request{position:absolute;left:902px;top:60px;width:262px;height:380px;background:var(--yellow-soft);border:1px solid #e8d78a;padding:12px 16px}
.request h3{font-size:13px;font-weight:700;color:var(--navy);text-align:center;margin-bottom:10px}
.field{background:var(--white);height:24px;margin-bottom:8px;font-size:9px;color:#888;padding:6px 8px}
.row2{display:flex;gap:8px}
.row2 .field{flex:1}
.area{height:70px}
.submit{background:var(--navy);color:var(--yellow);font-family:"Montserrat",Arial,sans-serif;font-weight:800;font-size:11px;text-align:center;padding:8px 0;width:110px;margin:4px auto 0}

/* content rows */
.school{position:absolute;left:0;top:1160px;width:1200px;height:220px;background:var(--grey-bg)}
.school h2,.diff h2{font-size:22px;font-weight:800;color:var(--navy)}
.school .copy{position:absolute;left:56px;top:60px;width:560px}
.copy p{font-size:11.5px;line-height:1.65;color:var(--muted);margin-top:10px}
.diff{position:absolute;left:0;top:1380px;width:1200px;height:300px}
.diff .copy{position:absolute;left:580px;top:40px;width:560px}
.pill{display:inline-block;margin-top:12px;background:var(--yellow);color:var(--navy);font-size:9px;font-weight:700;padding:5px 12px;border-radius:12px;font-family:"Montserrat",Arial,sans-serif}

/* savings */
.savings-title{position:absolute;left:0;top:1718px;width:1200px;text-align:center;font-size:26px;font-weight:800;color:var(--navy);font-family:"Montserrat",Arial,sans-serif}
.savings-title span{color:var(--yellow)}
.coupons{position:absolute;left:0;top:1780px;width:1200px;height:310px;background:var(--navy)}
.coupon{position:absolute;top:100px;color:var(--white)}
.coupon h3{font-size:17px;font-weight:700}
.coupon .save{color:var(--yellow);font-family:"Montserrat",Arial,sans-serif;font-weight:800;font-size:28px;margin-top:6px}
.coupon p{font-size:10px;color:#cdd3e4;margin-top:6px;width:200px;line-height:1.5}
.redeem{display:inline-block;margin-top:14px;border:1px solid var(--yellow);color:var(--yellow);font-size:9px;padding:4px 12px;border-radius:10px}
.divider{position:absolute;top:50px;width:1px;height:210px;background:var(--line)}

/* blogs */
.blogs{position:absolute;left:0;top:2090px;width:1200px;height:370px}
.blogs h2{position:absolute;left:0;top:40px;width:1200px;text-align:center;font-size:26px;font-weight:800;color:var(--navy)}
.blog-band{position:absolute;left:0;top:100px;width:1200px;height:250px;background:var(--yellow)}
.blog{position:absolute;top:20px;width:520px;height:210px;background:var(--cream);display:flex}
.blog .thumb{width:220px;height:210px;flex:none}
.blog .body{padding:16px 18px}
.blog .date{font-size:10px;color:var(--muted)}
.blog h3{font-size:15px;font-weight:700;color:var(--navy);margin-top:4px;line-height:1.3}
.blog p{font-size:11px;line-height:1.55;color:var(--muted);margin-top:8px}
.blog .btn-n{display:inline-block;margin-top:12px;border-radius:12px;font-size:9px;padding:5px 14px}
.chev{position:absolute;top:112px;width:20px;height:26px}

/* footer */
.footer{position:absolute;left:0;top:2460px;width:1200px;height:332px;background:var(--navy);color:var(--white)}
.footer .brand{left:40px;top:40px}
.footer .brand-name{color:var(--white);font-size:24px}
.footer .brand-dot{width:40px;height:40px}
.f-info{position:absolute;top:42px;display:flex;align-items:flex-start;gap:10px;font-size:13px;line-height:1.5}
.pay{position:absolute;left:920px;top:46px;display:flex;gap:8px}
.pay div{width:50px;height:32px;background:var(--white);border-radius:3px}
.rule{position:absolute;left:40px;top:104px;width:1120px;height:1px;background:var(--line)}
.f-note{position:absolute;left:330px;top:118px;font-size:12.5px;font-weight:700;color:var(--yellow)}
.f-links,.f-towns{position:absolute;top:152px;font-size:13px;line-height:1.7;list-style:none}
.f-links{left:40px}
.copyright{position:absolute;left:880px;top:152px;width:280px;font-size:12px;line-height:1.6;color:#d7dbe7}
</style>
</head>
<body>

<header class="topbar">
  <div class="brand"><span class="brand-dot"></span><span class="brand-name">RT Plumbing</span></div>
  <div class="serving">Serving Westbrook, MA &amp; Neighboring Communities</div>
  <div class="top-btns"><span class="btn-y">Request Service</span><span class="btn-n">Request a Quote</span></div>
  <div class="phones">
    <div><svg width="11" height="11" viewBox="0 0 24 24"><path fill="#0f1f4b" d="M6.6 10.8a15 15 0 0 0 6.6 6.6l2.2-2.2c.3-.3.7-.4 1-.2 1.1.4 2.3.6 3.6.6.6 0 1 .4 1 1V20c0 .6-.4 1-1 1A17 17 0 0 1 3 4c0-.6.4-1 1-1h3.5c.6 0 1 .4 1 1 0 1.3.2 2.5.6 3.6.1.3 0 .7-.2 1z"/></svg>555.013.7290</div>
    <div><svg width="11" height="11" viewBox="0 0 24 24"><path fill="#0f1f4b" d="M6.6 10.8a15 15 0 0 0 6.6 6.6l2.2-2.2c.3-.3.7-.4 1-.2 1.1.4 2.3.6 3.6.6.6 0 1 .4 1 1V20c0 .6-.4 1-1 1A17 17 0 0 1 3 4c0-.6.4-1 1-1h3.5c.6 0 1 .4 1 1 0 1.3.2 2.5.6 3.6.1.3 0 .7-.2 1z"/></svg>555.016.8841</div>
  </div>
</header>

<nav class="nav">
  <a class="active">Home</a><a>Plumbing</a><a>Water Heaters</a><a>Heating</a><a>Air Conditioning</a><a>Indoor Air Quality</a><a>Commercial</a><a>Handy Work &amp; Remodeling</a><a>Contact</a>
</nav>

<section class="hero">
  <div class="ph" role="img" aria-label="Smiling plumber in a cap holding a wrench" style="left:360px;top:0;width:420px;height:504px;background:linear-gradient(160deg,#3d4f7a,#1c2c58 60%,#0f1f4b)"></div>
  <div class="ph" role="img" aria-label="Technician servicing an outdoor air conditioning unit" style="left:800px;top:10px;width:170px;height:236px;background:linear-gradient(135deg,#b9b4a6,#6e6a60)"></div>
  <div class="ph" role="img" aria-label="Plumber fixing pipes under a kitchen sink" style="left:980px;top:10px;width:210px;height:236px;background:linear-gradient(135deg,#d7cfc0,#8a7f70)"></div>
  <div class="ph" role="img" aria-label="Worker installing a water heater" style="left:800px;top:256px;width:170px;height:238px;background:linear-gradient(135deg,#c6c2b8,#77746c)"></div>
  <div class="ph" role="img" aria-label="Bright renovated living room" style="left:980px;top:256px;width:210px;height:238px;background:linear-gradient(135deg,#efe8da,#a99b84)"></div>
  <div class="hero-copy">
    <div class="kicker">Enjoy the Best of</div>
    <h1>Home Living.<br>Indoors &amp; Out.</h1>
    <span class="btn-y">Contact Us to Get Started</span>
  </div>
</section>

<section class="services">
  <h2>More of What You Need</h2>
  <div class="svc-grid">
    <div class="svc"><div class="svc-ico"><svg width="22" height="22" viewBox="0 0 24 24"><path fill="#fff" d="M4 10h10v4H4zm10-4h4v12h-4z"/></svg></div><div class="svc-label">Plumbing</div><div class="svc-arrow"><svg width="18" height="14" viewBox="0 0 18 14"><path d="M0 7h14M9 1l6 6-6 6" stroke="#fff" stroke-width="2.4" fill="none"/></svg></div></div>
    <div class="svc"><div class="svc-ico"><svg width="22" height="22" viewBox="0 0 24 24"><path d="M3 8h12a3 3 0 1 0-3-3M3 13h16a3 3 0 1 1-3 3M3 18h8" stroke="#fff" stroke-width="2" fill="none"/></svg></div><div class="svc-label">Indoor Air Quality</div><div class="svc-arrow"><svg width="18" height="14" viewBox="0 0 18 14"><path d="M0 7h14M9 1l6 6-6 6" stroke="#fff" stroke-width="2.4" fill="none"/></svg></div></div>
    <div class="svc"><div class="svc-ico"><svg width="22" height="22" viewBox="0 0 24 24"><rect x="7" y="3" width="10" height="18" rx="4" fill="#fff"/></svg></div><div class="svc-label">Water Heaters</div><div class="svc-arrow"><svg width="18" height="14" viewBox="0 0 18 14"><path d="M0 7h14M9 1l6 6-6 6" stroke="#fff" stroke-width="2.4" fill="none"/></svg></div></div>
    <div class="svc"><div class="svc-ico"><svg width="22" height="22" viewBox="0 0 24 24"><path fill="#fff" d="M12 3s6 7 6 11a6 6 0 0 1-12 0c0-4 6-11 6-11z"/></svg></div><div class="svc-label">Water Filtration</div><div class="svc-arrow"><svg width="18" height="14" viewBox="0 0 18 14"><path d="M0 7h14M9 1l6 6-6 6" stroke="#fff" stroke-width="2.4" fill="none"/></svg></div></div>
    <div class="svc"><div class="svc-ico"><svg width="22" height="22" viewBox="0 0 24 24"><path fill="#fff" d="M12 2c1 4 6 6 6 12a6 6 0 0 1-12 0c0-3 2-5 3-6 0 2 1 3 2 3 0-3 0-6 1-9z"/></svg></div><div class="svc-label">Heating</div><div class="svc-arrow"><svg width="18" height="14" viewBox="0 0 18 14"><path d="M0 7h14M9 1l6 6-6 6" stroke="#fff" stroke-width="2.4" fill="none"/></svg></div></div>
    <div class="svc"><div class="svc-ico"><svg width="22" height="22" viewBox="0 0 24 24"><path fill="#fff" d="M3 12 12 4l9 8h-3v8H6v-8z"/></svg></div><div class="svc-label">Remodeling &amp;<br>Handy Work</div><div class="svc-arrow"><svg width="18" height="14" viewBox="0 0 18 14"><path d="M0 7h14M9 1l6 6-6 6" stroke="#fff" stroke-width="2.4" fill="none"/></svg></div></div>
    <div class="svc"><div class="svc-ico"><svg width="22" height="22" viewBox="0 0 24 24"><path d="M12 2v20M3 7l18 10M21 7 3 17" stroke="#fff" stroke-width="2"/></svg></div><div class="svc-label">Air Conditioning</div><div class="svc-arrow"><svg width="18" height="14" viewBox="0 0 18 14"><path d="M0 7h14M9 1l6 6-6 6" stroke="#fff" stroke-width="2.4" fill="none"/></svg></div></div>
    <div class="svc"><div class="svc-ico"><svg width="22" height="22" viewBox="0 0 24 24"><path fill="#fff" d="M4 4h16v16h-4v-6H8v6H4z"/></svg></div><div class="svc-label">Gas Fireplaces</div><div class="svc-arrow"><svg width="18" height="14" viewBox="0 0 18 14"><path d="M0 7h14M9 1l6 6-6 6" stroke="#fff" stroke-width="2.4" fill="none"/></svg></div></div>
  </div>
  <div class="ph" role="img" aria-label="Handyman with tool belt and hard hat giving a thumbs up" style="left:700px;top:110px;width:190px;height:420px;background:linear-gradient(180deg,#e3c56a,#4a5c86 55%,#2b3a61)"></div>
  <form class="request">
    <h3>Request Service</h3>
    <div class="field">Name</div>
    <div class="field">Email</div>
    <div class="field">Phone</div>
    <div class="field">Address</div>
    <div class="row2"><div class="field">City</div><div class="field">Zip</div></div>
    <div class="field">Service Needed</div>
    <div class="field area">Comments</div>
    <div class="submit">SUBMIT</div>
  </form>
</section>

<section class="school">
  <div class="copy">
    <h2>Back to School Reminder</h2>
    <p>Most families see an uptick in morning "rush hour" activity once the school year begins, and no one likes a cold shower. Can yours keep up with the increased demand? Contact us today for a water heater check-up and free quote on a replacement system.</p>
  </div>
  <div class="ph" role="img" aria-label="Close-up of a water heater tank in a basement" style="left:700px;top:20px;width:300px;height:180px;background:linear-gradient(135deg,#f3d9b8,#c98d5a)"></div>
</section>

<section class="diff">
  <div class="ph" role="img" aria-label="Modern open living room and kitchen interior" style="left:112px;top:50px;width:310px;height:200px;background:linear-gradient(135deg,#d9d5cc,#7d766b)"></div>
  <div class="copy">
    <h2>The RT Difference Makers</h2>
    <p>RT is a favorite choice among homeowners who appreciate our extensive range of home comfort and related services. Others like us best for our 100% satisfaction guarantee, while still others enjoy the many benefits that membership in our Preferred Service Club provides. Add it all up, and there's a lot to like about RT Plumbing, Heating, AC &amp; Remodeling.</p>
    <span class="pill">Learn More</span>
  </div>
</section>

<div class="savings-title">Enjoy the Savings...<span>Plus the Added Comfort!</span></div>

<section class="coupons">
  <div class="coupon" style="left:28px"><h3>New Water Heater</h3><div class="save">Save $120</div><p>on a new water heater, tank style or tankless</p></div>
  <div class="ph" role="img" aria-label="White tank water heater" style="left:280px;top:40px;width:100px;height:230px;background:linear-gradient(90deg,#cfd4dc,#ffffff 45%,#aeb5c0)"></div>
  <div class="divider" style="left:400px"></div>
  <div class="coupon" style="left:428px"><h3>HVAC System</h3><div class="save">Save $350</div><p>on a new heating or cooling system</p><span class="redeem">Click to Redeem</span></div>
  <div class="ph" role="img" aria-label="Furnace and air handler unit" style="left:680px;top:40px;width:110px;height:230px;background:linear-gradient(90deg,#9aa2ad,#e7e9ec 50%,#7d8590)"></div>
  <div class="divider" style="left:810px"></div>
  <div class="coupon" style="left:838px"><h3>First-time Customer</h3><div class="save">Save $35</div><p>on any service we provide</p></div>
  <div class="ph" role="img" aria-label="Compact tankless water heater" style="left:1080px;top:50px;width:100px;height:210px;background:linear-gradient(90deg,#c8cdd4,#ffffff 45%,#a9b0ba)"></div>
</section>

<section class="blogs">
  <h2>Latest Blogs</h2>
  <div class="blog-band">
    <svg class="chev" style="left:12px" viewBox="0 0 20 26"><path d="M15 2 4 13l11 11" stroke="#0f1f4b" stroke-width="3" fill="none"/></svg>
    <svg class="chev" style="left:1168px" viewBox="0 0 20 26"><path d="M5 2l11 11L5 24" stroke="#0f1f4b" stroke-width="3" fill="none"/></svg>
    <article class="blog" style="left:50px">
      <div class="thumb" role="img" aria-label="Modern white toilet in a bathroom" style="background:linear-gradient(135deg,#eae6de,#a8a196)"></div>
      <div class="body">
        <div class="date">April 27, 2023</div>
        <h3>How to Choose the Best Toilet Style</h3>
        <p>It may seem like such a simple purchase but buying a toilet can be quite overwhelming.</p>
        <span class="btn-n">Read More</span>
      </div>
    </article>
    <article class="blog" style="left:630px">
      <div class="thumb" role="img" aria-label="Technician checking an air conditioner" style="background:linear-gradient(135deg,#d6dbe2,#7f8a99)"></div>
      <div class="body">
        <div class="date">May 16, 2023</div>
        <h3>The Benefits of an AC Tune-Up</h3>
        <p>How do you prepare your home for spring and summer? Let's see, there's the time-honored tradition of spring cleaning.</p>
        <span class="btn-n">Read More</span>
      </div>
    </article>
  </div>
</section>

<footer class="footer">
  <div class="brand"><span class="brand-dot"></span><span class="brand-name">RT Plumbing</span></div>
  <div class="f-info" style="left:430px">
    <svg width="16" height="20" viewBox="0 0 16 20"><path fill="#f7cf1c" d="M8 0a8 8 0 0 1 8 8c0 6-8 12-8 12S0 14 0 8a8 8 0 0 1 8-8zm0 5a3 3 0 1 0 0 6 3 3 0 0 0 0-6z"/></svg>
    <div>118 Cedar Street<br>Millbrook, MA 01899</div>
  </div>
  <div class="f-info" style="left:680px">
    <svg width="16" height="16" viewBox="0 0 24 24"><path fill="#f7cf1c" d="M6.6 10.8a15 15 0 0 0 6.6 6.6l2.2-2.2c.3-.3.7-.4 1-.2 1.1.4 2.3.6 3.6.6.6 0 1 .4 1 1V20c0 .6-.4 1-1 1A17 17 0 0 1 3 4c0-.6.4-1 1-1h3.5c.6 0 1 .4 1 1 0 1.3.2 2.5.6 3.6.1.3 0 .7-.2 1z"/></svg>
    <div>555.013.7290<br>555.016.8841</div>
  </div>
  <div class="pay"><div></div><div></div><div></div><div></div></div>
  <div class="rule"></div>
  <div class="f-note">Providing service throughout the greater Millbrook area, including right here:</div>
  <ul class="f-links"><li>Home</li><li>About Us</li><li>Testimonials</li><li>Contact Us</li></ul>
  <ul class="f-towns" style="left:330px"><li>Ashgrove</li><li>Bellrock</li><li>Brookhollow</li><li>Dunmore</li><li>Fernwick</li></ul>
  <ul class="f-towns" style="left:470px"><li>Linden Falls</li><li>Marlowe</li><li>Northby</li><li>Newmarsh</li></ul>
  <ul class="f-towns" style="left:610px"><li>Stillbury</li><li>Wexford Hills</li><li>Willowmere</li><li>Westcliff</li></ul>
  <div class="copyright">© 2023 RT Plumbing &amp; Heating. All Rights Reserved.</div>
</footer>

</body>
</html>
```